Australian Raw Honey Label Design for Florvane Honey

We need a new label design for our honey jars. Previous label was very amateurish and we need a new more professional look. We are also changing name to Florvane; which means kiss in French. The label should be simple, fluid, with simple drawings of flowers, bees in the décor reflecting the minimal process we use in producing our honey.
I would like to use my profile (curly/afro hair) (that people can recognise ) that connects with bees. The colour scheme should be warm sun, yellow or orange without too many colours or heavy background.

Label size: 200 mm x 60 mm
there are two variantes of the label, one with 1kg and the other with 500g
More information in the attached brief.

Target Market(s)

customer looking for locally produced honey vs commercial supermarket honey. Product sold mostly through word of mouth

Colors
ffc214
f78f20
f68e4e
fbed22

Requirements
Must have
• Included in the brief as per food label requirement
Nice to have
• curve, flowy font for brand name
• Brand means kiss, so connection with bees is important.
Should not have
• heavy background colors

```html
<!DOCTYPE html>
<html lang="en">
<head>
<meta charset="utf-8">
<title>Florvane Honey – Jar Label</title>
<link href="https://fonts.googleapis.com/css2?family=Alegreya:wght@500;700&display=swap" rel="stylesheet">
<style>
  :root {
    --page: #ffffff;
    --frame: #4a4a4a;
    --rim-brown: #8a5a2b;
    --rim-light: #b97a3c;
    --honey: #ffc214;
    --honey-soft: #ffe680;
    --honey-pale: #fff3b8;
    --brand-red: #e0312f;
    --weight-red: #d6253a;
    --tagline: #85663a;
    --emblem-dark: #9c7a34;
  }
  * { margin: 0; padding: 0; box-sizing: border-box; }
  html, body { width: 1200px; height: 801px; overflow: hidden; background: var(--page); }
  .canvas {
    position: relative;
    width: 1200px;
    height: 801px;
    border: 2px solid var(--frame);
    background: var(--page);
  }
  .label-shape { position: absolute; left: 0; top: 0; }
  .brand-name {
    position: absolute;
    left: 0; width: 1200px; top: 246px;
    text-align: center;
    font-family: "Alegreya", Georgia, serif;
    font-weight: 700;
    font-size: 64px;
    color: var(--brand-red);
    line-height: 1;
  }
  .emblem {
    position: absolute;
    left: 524px; top: 332px;
    width: 152px; height: 146px;
    border-radius: 50%;
    background: radial-gradient(circle at 50% 45%, #3a3a3a 0 18%, var(--emblem-dark) 19% 62%, rgba(156,122,52,0.35) 63% 100%);
  }
  .tagline-strip {
    position: absolute;
    left: 415px; top: 494px;
    width: 370px; height: 48px;
    background: linear-gradient(90deg, rgba(255,255,255,0) 0%, rgba(255,255,255,0.85) 35%, rgba(255,255,255,0.95) 55%, rgba(255,255,255,0) 100%);
    border-top: 2px solid rgba(255,230,140,0.8);
    border-bottom: 2px solid rgba(255,230,140,0.8);
  }
  .tagline {
    position: absolute;
    left: 0; width: 1200px; top: 500px;
    text-align: center;
    font-family: "Alegreya", Georgia, serif;
    font-weight: 700;
    font-size: 29px;
    color: var(--tagline);
    line-height: 1.2;
  }
  .net-weight {
    position: absolute;
    left: 0; width: 1200px; top: 591px;
    text-align: center;
    font-family: "Alegreya", Georgia, serif;
    font-weight: 700;
    font-size: 21px;
    color: var(--weight-red);
    line-height: 1.2;
  }
</style>
</head>
<body>
<div class="canvas">
  <svg class="label-shape" width="1200" height="801" viewBox="0 0 1200 801" aria-hidden="true">
    <defs>
      <linearGradient id="rim" x1="0" x2="1" y1="0" y2="0">
        <stop offset="0" stop-color="var(--rim-brown)"/>
        <stop offset="0.5" stop-color="var(--rim-light)"/>
        <stop offset="1" stop-color="var(--rim-brown)"/>
      </linearGradient>
      <radialGradient id="band-glow" cx="0.5" cy="0.45" r="0.6">
        <stop offset="0" stop-color="var(--honey-pale)"/>
        <stop offset="0.45" stop-color="var(--honey-soft)"/>
        <stop offset="1" stop-color="var(--honey)"/>
      </radialGradient>
    </defs>
    <!-- band rim -->
    <rect x="85" y="251" width="1032" height="360" fill="url(#rim)"/>
    <!-- central plaque -->
    <path d="M440,215 L485,215 Q490,215 493,208 C520,172 560,162 600,162 C640,162 680,172 707,208 Q710,215 715,215 L760,215 Q782,215 782,237 L782,618 Q782,640 760,640 L440,640 Q418,640 418,618 L418,237 Q418,215 440,215 Z"
          fill="var(--honey-soft)" stroke="var(--rim-brown)" stroke-width="12"/>
    <path d="M442,224 L487,224 Q496,224 500,215 C526,182 562,172 600,172 C638,172 674,182 700,215 Q704,224 713,224 L758,224 Q773,224 773,239 L773,616 Q773,631 758,631 L442,631 Q427,631 427,616 L427,239 Q427,224 442,224 Z"
          fill="none" stroke="var(--honey)" stroke-width="4"/>
    <!-- band body -->
    <rect x="85" y="259" width="1032" height="344" fill="url(#band-glow)"/>
  </svg>

  <div class="brand-name">Florvane</div>
  <div class="emblem" role="img" aria-label="Illustrated bee with wings spread over a circle of line-drawn flowers and leaves"></div>
  <div class="tagline-strip"></div>
  <div class="tagline">Premium Raw Honey</div>
  <div class="net-weight">500 gm Net wt</div>
</div>
</body>
</html>
```